Fernwood Chiropractic
letterhead/business cards
Project: Fernwood Chiropractic
Fernwood Chiropractic - Health
Creative Brief
Professional
Dr. Gavin P. Holcombe
Chiropractor
4817 Dunmore Road Building 2, Suite C-21 Philadelphia, PA 19144
drholcombe@fernwoodchiro-example.com
www.fernwoodchiro-example.com

```html
<!DOCTYPE html>
<html lang="en">
<head>
<meta charset="utf-8">
<title>Fernwood Chiropractic – Business Cards</title>
<link rel="stylesheet" href="https://fonts.googleapis.com/css2?family=Cinzel:wght@400;700&display=swap">
<style>
  :root {
    --bg: #e9eaeb;
    --card: #ffffff;
    --green: #3a9b3f;
    --blue: #1d4f9c;
    --leaf: #6fb33a;
    --ink-white: #ffffff;
    --shadow: rgba(0,0,0,0.18);
  }
  * { margin: 0; padding: 0; box-sizing: border-box; }
  html, body { width: 1200px; height: 874px; overflow: hidden; background: var(--bg); }
  body { font-family: "Cinzel", Georgia, serif; position: relative; }

  .card {
    position: absolute;
    left: 250px;
    width: 700px;
    height: 400px;
    background: var(--card);
    border-radius: 26px;
    overflow: hidden;
    box-shadow: 0 6px 18px var(--shadow);
  }
  .card--back { top: 22px; }
  .card--front { top: 452px; }

  .card-shapes { position: absolute; inset: 0; width: 100%; height: 100%; }

  .brand {
    position: absolute;
    display: flex;
    align-items: center;
    gap: 14px;
  }
  .brand-dot {
    width: 34px; height: 34px;
    border-radius: 50%;
    background: var(--leaf);
    flex: none;
  }
  .brand-name {
    color: var(--blue);
    font-weight: 700;
    font-size: 30px;
    line-height: 1.05;
    letter-spacing: 0.5px;
  }
  .card--back .brand { left: 70px; top: 150px; }
  .card--front .brand { left: 36px; top: 160px; }
  .card--front .brand-name { font-size: 25px; }

  .back-web {
    position: absolute;
    right: 40px;
    bottom: 36px;
    color: var(--blue);
    font-size: 17px;
    letter-spacing: 0.5px;
  }

  .details {
    position: absolute;
    left: 430px;
    top: 48px;
    right: 24px;
    color: var(--ink-white);
  }
  .person-name { font-size: 21px; font-weight: 400; letter-spacing: 0.5px; }
  .person-title { font-size: 14px; margin-top: 6px; letter-spacing: 0.5px; }

  .contact-list { list-style: none; margin-top: 56px; }
  .contact-item {
    display: flex;
    align-items: flex-start;
    gap: 10px;
    font-size: 12px;
    line-height: 1.35;
    margin-bottom: 10px;
  }
  .contact-icon { flex: none; width: 18px; height: 18px; margin-top: 0; }
</style>
</head>
<body>

  <section class="card card--back" aria-label="Business card back">
    <div class="brand">
      <span class="brand-dot"></span>
      <span class="brand-name">Fernwood<br>Chiropractic</span>
    </div>
    <p class="back-web">www.fernwoodchiro-example.com</p>
  </section>

  <section class="card card--front" aria-label="Business card front">
    <svg class="card-shapes" viewBox="0 0 700 400" preserveAspectRatio="none" aria-hidden="true">
      <path d="M352 0 C300 90 304 320 338 400 L372 400 C338 320 336 90 392 0 Z" fill="var(--blue)"/>
      <path d="M400 0 C344 90 346 320 380 400 L700 400 L700 0 Z" fill="var(--green)"/>
    </svg>

    <div class="brand">
      <span class="brand-dot"></span>
      <span class="brand-name">Fernwood<br>Chiropractic</span>
    </div>

    <div class="details">
      <h1 class="person-name">Dr. Gavin P. Holcombe</h1>
      <p class="person-title">Chiropractor</p>

      <ul class="contact-list">
        <li class="contact-item">
          <svg class="contact-icon" viewBox="0 0 18 18"><circle cx="9" cy="9" r="9" fill="#fff"/><path d="M9 4a3 3 0 0 0-3 3c0 2.3 3 6 3 6s3-3.7 3-6a3 3 0 0 0-3-3zm0 4.2a1.2 1.2 0 1 1 0-2.4 1.2 1.2 0 0 1 0 2.4z" fill="var(--green)"/></svg>
          <span>4817 Dunmore Road<br>Building 2, Suite C-21<br>Philadelphia, PA 19144</span>
        </li>
        <li class="contact-item">
          <svg class="contact-icon" viewBox="0 0 18 18"><circle cx="9" cy="9" r="9" fill="#fff"/><path d="M6 4.5l1.6 0 .8 2.2-1 .9a6 6 0 0 0 2.9 2.9l.9-1 2.2.8v1.6c0 .6-.5 1-1 1A7.5 7.5 0 0 1 5 5.5c0-.5.4-1 1-1z" fill="var(--green)"/></svg>
          <span>(215) 555-0148</span>
        </li>
        <li class="contact-item">
          <svg class="contact-icon" viewBox="0 0 18 18"><circle cx="9" cy="9" r="9" fill="#fff"/><path d="M6 4.5l1.6 0 .8 2.2-1 .9a6 6 0 0 0 2.9 2.9l.9-1 2.2.8v1.6c0 .6-.5 1-1 1A7.5 7.5 0 0 1 5 5.5c0-.5.4-1 1-1z" fill="var(--green)"/></svg>
          <span>(215) 555-0193</span>
        </li>
        <li class="contact-item">
          <svg class="contact-icon" viewBox="0 0 18 18"><circle cx="9" cy="9" r="9" fill="#fff"/><rect x="4.5" y="6" width="9" height="6.5" rx="1" fill="var(--green)"/><path d="M4.8 6.4L9 9.6l4.2-3.2" stroke="#fff" stroke-width="0.9" fill="none"/></svg>
          <span>drholcombe@fernwoodchiro-example.com</span>
        </li>
        <li class="contact-item">
          <svg class="contact-icon" viewBox="0 0 18 18"><circle cx="9" cy="9" r="9" fill="#fff"/><circle cx="9" cy="9" r="4.5" fill="none" stroke="var(--green)" stroke-width="1.1"/><ellipse cx="9" cy="9" rx="2" ry="4.5" fill="none" stroke="var(--green)" stroke-width="1"/><path d="M4.5 9h9" stroke="var(--green)" stroke-width="1"/></svg>
          <span>www.fernwoodchiro-example.com</span>
        </li>
      </ul>
    </div>
  </section>

</body>
</html>
```